Dietitian needs awesome business card

I need a contemporary design that's eye catching but professional.
My card is to given to doctors, specialists and patients alike.
I manage patients with chronic diseases
I have uploaded my logo and current business card, I would also like the other Registered Clinical Nutritionist logo incorporated into the design

Target Market(s)

Doctors, specialists and patients

Industry/Entity Type

Healthcare

Contact Information for Business Card

www.brindlecovenutrition.com.au
Ph: 0427 516 903
Fax: 6482 7315
email: marcus.k.wellfare@quorvamail.com
Space on the back of the card with: Appointment date, Appointment time and appointment location

Font styles to use
Serif

Colors
fbee3e
876aae
ffc214

Requirements
Must have
• My Logo
• Registered Clinical Nutritionist Logo
• My 4 locations - Fernhollow Medical Centre, North Kelby Health, Ashcourt Medical, Pinebrook Doctors Surgery
Nice to have
• I like the colours in my current business card

```html
<!DOCTYPE html>
<html lang="en">
<head>
<meta charset="utf-8">
<title>Brindlecove Nutrition &amp; Dietetics – Business Card</title>
<link href="https://fonts.googleapis.com/css2?family=Fira+Sans:wght@400;500&display=swap" rel="stylesheet">
<style>
  :root {
    --backdrop: #dcdde0;
    --card: #ffffff;
    --lime: #9acd3c;
    --ink: #1c1c1c;
    --brand-blue: #1f6db5;
    --badge-tint: #f2f2f2;
    --rule: #111111;
  }
  * { box-sizing: border-box; margin: 0; padding: 0; }
  html, body { width: 1200px; height: 800px; overflow: hidden; }
  body {
    background: var(--backdrop);
    font-family: "Fira Sans", sans-serif;
    color: var(--ink);
    position: relative;
  }
  .card {
    position: absolute;
    top: 245px;
    width: 540px;
    height: 310px;
    background: var(--card);
    box-shadow: 0 6px 18px rgba(0,0,0,.12);
    overflow: hidden;
  }
  /* Appointment side */
  .card--appointment { left: 40px; }
  .appointment__brand {
    position: absolute; left: 250px; top: 58px;
    display: flex; align-items: center; gap: 10px;
    color: var(--brand-blue); font-weight: 500;
  }
  .brand-dot { width: 34px; height: 34px; border-radius: 50%; background: var(--brand-blue); }
  .appointment__brand .brand-name { font-size: 27px; line-height: 1; }
  .appointment__brand .brand-sub { font-size: 12px; line-height: 1.3; }
  .appointment__title {
    position: absolute; left: 48px; top: 88px;
    font-size: 17px; letter-spacing: .5px;
  }
  .field { position: absolute; font-size: 11px; }
  .field-line { position: absolute; height: 2px; background: var(--rule); }

  /* Identity side */
  .card--identity { left: 620px; }
  .identity__badge {
    position: absolute; left: 60px; top: -60px;
    width: 300px; height: 300px; border-radius: 50%;
    background: var(--badge-tint);
  }
  .identity__name {
    position: absolute; left: 36px; top: 160px;
    font-size: 24px; font-weight: 500;
  }
  .identity__role {
    position: absolute; left: 36px; top: 193px;
    font-size: 14px; color: var(--lime); letter-spacing: .4px;
  }
  .identity__panel {
    position: absolute; right: 0; top: 0;
    width: 262px; height: 100%;
    background: var(--lime); color: #fff;
    padding: 34px 20px 0 22px;
  }
  .panel__brand { display: flex; align-items: center; gap: 8px; margin-bottom: 16px; }
  .panel__brand .brand-dot { width: 30px; height: 30px; background: #fff; }
  .panel__brand .brand-name { font-size: 19px; line-height: 1.05; font-weight: 400; }
  .panel__brand .brand-sub { font-size: 9px; font-weight: 400; }
  .panel__locations { font-size: 11px; line-height: 1.5; margin-bottom: 14px; }
  .contact-list { list-style: none; font-size: 11px; }
  .contact-list li { display: flex; align-items: center; gap: 8px; margin-bottom: 9px; }
  .contact-list svg { width: 13px; height: 13px; flex: none; }
</style>
</head>
<body>

<section class="card card--appointment" aria-label="Appointment card">
  <div class="appointment__brand">
    <span class="brand-dot"></span>
    <div>
      <div class="brand-name">Brindlecove</div>
      <div class="brand-sub">Nutrition &amp; Dietetics</div>
    </div>
  </div>
  <h2 class="appointment__title">APPOINTMENT</h2>
  <span class="field" style="left:48px;top:140px">DATE:</span>
  <div class="field-line" style="left:48px;top:158px;width:444px"></div>
  <span class="field" style="left:300px;top:178px">TIME:</span>
  <span class="field" style="left:48px;top:210px">LOCATION:</span>
  <div class="field-line" style="left:48px;top:228px;width:444px"></div>
</section>

<section class="card card--identity" aria-label="Business card front">
  <div class="identity__badge" role="img" aria-label="Faint accreditation badge"></div>
  <h1 class="identity__name">Marcus Wellfare</h1>
  <p class="identity__role">NUTRITIONIST AND CHEF</p>

  <div class="identity__panel">
    <div class="panel__brand">
      <span class="brand-dot"></span>
      <div>
        <div class="brand-name">Brindlecove</div>
        <div class="brand-sub">Nutrition &amp; Dietetics</div>
      </div>
    </div>
    <p class="panel__locations">Fernhollow Medical Centre, North Kelby Health<br>Ashcourt Medical, Pinebrook Doctors Surgery</p>
    <ul class="contact-list">
      <li>
        <svg viewBox="0 0 24 24" aria-hidden="true"><path fill="#fff" d="M6.6 10.8a15 15 0 0 0 6.6 6.6l2.2-2.2a1 1 0 0 1 1-.25 11 11 0 0 0 3.6.6 1 1 0 0 1 1 1V20a1 1 0 0 1-1 1A17 17 0 0 1 3 4a1 1 0 0 1 1-1h3.5a1 1 0 0 1 1 1c0 1.25.2 2.45.6 3.6a1 1 0 0 1-.25 1z"/></svg>
        0427 516 903
      </li>
      <li>
        <svg viewBox="0 0 24 24" aria-hidden="true"><rect x="4" y="10" width="16" height="11" rx="1" fill="#fff"/><path d="M8 10V7a4 4 0 0 1 8 0" stroke="#fff" stroke-width="2" fill="none"/></svg>
        6482 7315
      </li>
      <li>
        <svg viewBox="0 0 24 24" aria-hidden="true"><rect x="2" y="5" width="20" height="14" rx="1" fill="#fff"/><path d="M2 6l10 7 10-7" stroke="#9acd3c" stroke-width="1.6" fill="none"/></svg>
        marcus.k.wellfare@quorvamail.com
      </li>
      <li>
        <svg viewBox="0 0 24 24" aria-hidden="true"><path d="M2 9a14 14 0 0 1 20 0M5.5 12.5a9 9 0 0 1 13 0M9 16a4 4 0 0 1 6 0" stroke="#fff" stroke-width="2" fill="none" stroke-linecap="round"/><circle cx="12" cy="19.5" r="1.6" fill="#fff"/></svg>
        www.brindlecovenutrition.com.au
      </li>
    </ul>
  </div>
</section>

</body>
</html>
```